KB Rubbish Removal Business Card

Hey,
I need a double sided business card designed for a rubbish removal business based in Australia. Logo is already chosen, similar colours preferred for both sides of the business card.

Details to include:

Front:

KB Rubbish Removal
Darren Holloway
Managing Director
Mobile: 0471 902 146
Email: darren@kbrubbishremoval.com.au
Website: kbrubbishremoval.com.au

Rear:

How did we do?
kbrubbishremoval.com.au/review

```html
<!DOCTYPE html>
<html lang="en">
<head>
<meta charset="UTF-8">
<title>KB Rubbish Removal – Business Card</title>
<link href="https://fonts.googleapis.com/css2?family=Montserrat:wght@500;600;700&display=swap" rel="stylesheet">
<style>
  :root {
    --page-bg: #ffffff;
    --label-green: #1a8c2a;
    --card-dark: #006a12;
    --card-mid: #0f9a2c;
    --card-light: #1bb840;
    --mark-dark: #03620f;
    --mark-light: #33c24f;
    --ink-white: #ffffff;
  }
  * { margin: 0; padding: 0; box-sizing: border-box; }
  html, body {
    width: 1200px;
    height: 1200px;
    overflow: hidden;
    background: var(--page-bg);
    font-family: "Montserrat", Arial, sans-serif;
  }
  .sheet { position: relative; width: 1200px; height: 1200px; }

  .side-label {
    position: absolute;
    top: 386px;
    width: 200px;
    margin-left: -100px;
    text-align: center;
    font-size: 19px;
    font-weight: 700;
    color: var(--label-green);
    letter-spacing: 0.5px;
  }
  .side-label--rear { left: 318px; }
  .side-label--front { left: 880px; }

  .card {
    position: absolute;
    top: 460px;
    width: 490px;
    height: 280px;
    overflow: hidden;
    background: linear-gradient(90deg, var(--card-dark) 0%, var(--card-mid) 45%, var(--card-light) 100%);
    color: var(--ink-white);
  }
  .card--rear { left: 74px; }
  .card--front { left: 636px; }

  /* rear */
  .rear-dot {
    position: absolute;
    left: 30px;
    top: 112px;
    width: 62px;
    height: 62px;
    border-radius: 50%;
    background: var(--mark-light);
  }
  .rear-name {
    position: absolute;
    left: 101px;
    top: 120px;
    font-size: 33px;
    font-weight: 700;
    white-space: nowrap;
    line-height: 1;
  }

  /* front */
  .front-glow {
    position: absolute;
    inset: 0;
    background: radial-gradient(circle at 30% 50%, rgba(0,0,0,0) 0 40%, rgba(60,190,70,0.35) 41% 60%, rgba(0,0,0,0) 61%);
  }
  .front-dot {
    position: absolute;
    left: 31px;
    top: 74px;
    width: 120px;
    height: 120px;
    border-radius: 50%;
    background: var(--mark-dark);
  }
  .front-divider {
    position: absolute;
    left: 181px;
    top: 38px;
    width: 1.5px;
    height: 202px;
    background: var(--ink-white);
  }
  .front-info {
    position: absolute;
    left: 210px;
    top: 0;
    white-space: nowrap;
  }
  .front-info p { position: absolute; left: 0; line-height: 1; }
  .company { top: 58px; font-size: 13px; font-weight: 600; }
  .person { top: 95px; font-size: 18px; font-weight: 700; }
  .role { top: 114px; font-size: 13px; font-weight: 600; }
  .contact { font-size: 13px; font-weight: 600; }
  .contact--mobile { top: 153px; }
  .contact--email { top: 171px; }
  .contact--web { top: 206px; }
</style>
</head>
<body>
<main class="sheet">
  <div class="side-label side-label--rear">REAR</div>
  <div class="side-label side-label--front">FRONT</div>

  <section class="card card--rear">
    <span class="rear-dot"></span>
    <p class="rear-name">KB Rubbish Removal</p>
  </section>

  <section class="card card--front">
    <div class="front-glow"></div>
    <span class="front-dot"></span>
    <span class="front-divider"></span>
    <div class="front-info">
      <p class="company">KB Rubbish Removal</p>
      <p class="person">Darren Holloway</p>
      <p class="role">Managing Director</p>
      <p class="contact contact--mobile">Mobile: 0471 902 146</p>
      <p class="contact contact--email">darren@kbrubbishremoval.com.au</p>
      <p class="contact contact--web">www.kbrubbishremoval.com.au</p>
    </div>
  </section>
</main>
</body>
</html>
```